Poster Design For Obstacle Run

Design a poster for the Crow Ridge Obstacle run.
Text: Crow Ridge Obstacle Run. May 12th, 2018. Sittard. www.crowridgedash.nl. I have added a lot of pictures.
Furthermore, the logo should be included. As an example I included a poster from the ironbark race that we really like (ironbark team challenge) and also. Feel free to take a look at our website for inspiration: www.crowridgedash.nl

```html
<!DOCTYPE html>
<html lang="en">
<head>
<meta charset="utf-8">
<title>Crow Ridge Obstacle Run – Poster</title>
<link href="https://fonts.googleapis.com/css2?family=Oswald:wght@500;600&family=Rubik+Dirt&display=swap" rel="stylesheet">
<style>
  :root {
    --backdrop: #dfe5e4;
    --poster-black: #141210;
    --poster-brown: #241c17;
    --orange: #f0642a;
    --white: #ffffff;
    --band-light: #d9d9d9;
    --band-dark: #3a3a3a;
    --ink: #1b1b1b;
  }
  * { margin: 0; padding: 0; box-sizing: border-box; }
  html, body {
    width: 1200px; height: 1200px; overflow: hidden;
    background: var(--backdrop);
  }
  .poster {
    position: absolute; left: 207px; top: 30px;
    width: 786px; height: 1140px; overflow: hidden;
    background:
      radial-gradient(ellipse at 50% 75%, var(--poster-brown) 0%, var(--poster-black) 70%);
    font-family: "Oswald", sans-serif;
  }
  .hero-frame { position: absolute; left: 0; top: 0; width: 786px; height: 660px; }
  .event-mark {
    position: absolute; left: 0; right: 0; top: 790px;
    text-align: center; color: var(--orange);
    font-family: "Oswald", sans-serif; font-weight: 600;
    font-size: 36px; line-height: 1.1; letter-spacing: 3px;
  }
  .event-title {
    position: absolute; left: 0; right: 0; top: 918px;
    text-align: center; font-family: "Rubik Dirt", sans-serif; font-weight: 400;
    font-size: 44px; line-height: 1; white-space: nowrap;
  }
  .event-title .accent { color: var(--orange); }
  .event-title .main { color: var(--white); }
  .date-band {
    position: absolute; left: 169px; top: 1001px; width: 457px; height: 55px;
    background: linear-gradient(90deg, rgba(60,60,60,0) 0%, var(--band-dark) 12%, var(--band-light) 45%, var(--band-light) 60%, var(--band-dark) 88%, rgba(60,60,60,0) 100%);
    display: flex; align-items: center; justify-content: center; gap: 22px;
  }
  .date-band .stars { color: var(--orange); font-size: 20px; letter-spacing: 3px; }
  .date-band .date {
    color: var(--ink); font-weight: 600; font-size: 40px; letter-spacing: -0.5px;
  }
  .info-line {
    position: absolute; left: 0; right: 0; top: 1084px;
    display: flex; justify-content: center; align-items: center; gap: 26px;
    color: var(--white); font-weight: 500; font-size: 19px; letter-spacing: 6px;
  }
  .info-item { display: flex; align-items: center; gap: 10px; }
  .info-item svg { flex: none; }
</style>
</head>
<body>
  <main class="poster">
    <svg class="hero-frame" viewBox="0 0 786 660" xmlns="http://www.w3.org/2000/svg">
      <defs>
        <linearGradient id="mudPhoto" x1="0" y1="0" x2="1" y2="1">
          <stop offset="0" stop-color="#a89b8a"/>
          <stop offset="0.45" stop-color="#6e4c38"/>
          <stop offset="0.75" stop-color="#c8542a"/>
          <stop offset="1" stop-color="#3a2a22"/>
        </linearGradient>
      </defs>
      <ellipse cx="400" cy="296" rx="338" ry="304" fill="none" stroke="var(--white)" stroke-width="12"/>
      <ellipse cx="396" cy="284" rx="332" ry="300" fill="none" stroke="var(--orange)" stroke-width="14"/>
      <ellipse cx="398" cy="286" rx="322" ry="292" fill="url(#mudPhoto)" role="img" aria-label="Photo: mud-covered runner in an orange shirt climbing a rope up a wooden wall"/>
    </svg>

    <div class="event-mark">CROW RIDGE<br>OBSTACLE RUN</div>

    <h1 class="event-title"><span class="accent">Crow Ridge</span> <span class="main">OBSTACLE RUN</span></h1>

    <div class="date-band">
      <span class="stars">★★★</span>
      <span class="date">MAY 12TH, 2018</span>
      <span class="stars">★★★</span>
    </div>

    <div class="info-line">
      <span class="info-item">
        <svg width="18" height="18" viewBox="0 0 20 20"><circle cx="10" cy="10" r="8" fill="none" stroke="var(--orange)" stroke-width="2"/><ellipse cx="10" cy="10" rx="3.5" ry="8" fill="none" stroke="var(--orange)" stroke-width="1.6"/><line x1="2" y1="10" x2="18" y2="10" stroke="var(--orange)" stroke-width="1.6"/></svg>
        WWW.CROWRIDGEDASH.NL
      </span>
      <span class="info-item">
        <svg width="16" height="20" viewBox="0 0 16 20"><path d="M8 1a6.5 6.5 0 0 0-6.5 6.5C1.5 12 8 19 8 19s6.5-7 6.5-11.5A6.5 6.5 0 0 0 8 1z" fill="none" stroke="var(--orange)" stroke-width="2"/><circle cx="8" cy="7.5" r="2.2" fill="var(--orange)"/></svg>
        SITTARD
      </span>
    </div>
  </main>
</body>
</html>
```